Peanut Butter for Dogs - Label

Dear Designers,

Our company develops natural & innovative products aimed at enhancing animal (cat & dog) well-being. The company focuses on producing high-end, ethically sourced products that naturally soothe pets, improving their quality of life.

We are currently developing a new CBD-enriched Peanut Butter product for dogs, and we are looking for some label designs that follow our brand image & brand identity.

-> Please see full brief PDF file attached.

Target Market(s)

European Market (French Speaking)

Industry/Entity Type

Pet Food

Font styles to use
Other font styles liked:
• Please see brand kit in PDF brief

Colors

Designer to choose colors to be used in the design.

Requirements
Must have
• Please see brief PDF file attached
Nice to have
Should not have

```html
<!DOCTYPE html>
<html lang="fr">
<head>
<meta charset="utf-8">
<title>Verdalis – Tendresse Apaisante</title>
<link rel="stylesheet" href="https://fonts.googleapis.com/css2?family=Roboto+Slab:wght@500&family=Quicksand:wght@500;600;700&display=swap">
<style>
  :root {
    --cream: #f9f1e7;
    --paper: #ffffff;
    --teal: #3a9a78;
    --teal-dark: #2c8a66;
    --teal-light: #5bb194;
    --ink: #333333;
    --white: #ffffff;
  }
  * { box-sizing: border-box; margin: 0; padding: 0; }
  html, body { width: 1198px; height: 1200px; overflow: hidden; }
  body {
    background: var(--cream);
    position: relative;
    font-family: "Quicksand", sans-serif;
  }
  .label {
    position: absolute;
    left: 159px; top: 260px;
    width: 880px; height: 680px;
    background: var(--paper);
    overflow: hidden;
    box-shadow: 0 10px 30px rgba(120, 100, 70, 0.12);
  }
  .label__rule {
    position: absolute; left: 0; top: 30px;
    width: 880px; height: 90px;
  }
  .brand {
    position: absolute; left: 0; width: 100%; top: 200px;
    text-align: center;
  }
  .brand__name {
    font-family: "Roboto Slab", serif;
    font-weight: 500;
    font-size: 56px;
    letter-spacing: 1px;
    color: var(--ink);
    line-height: 1;
  }
  .brand__tagline {
    font-family: "Roboto Slab", serif;
    font-weight: 500;
    font-size: 19px;
    color: var(--teal);
    margin-top: 6px;
    padding-left: 180px;
  }
  .product {
    position: absolute; left: 0; width: 100%; top: 355px;
    text-align: center;
  }
  .product__name {
    font-weight: 700;
    font-size: 38px;
    color: var(--teal);
    letter-spacing: 0.5px;
  }
  .product__dose {
    font-weight: 500;
    font-size: 35px;
    color: var(--ink);
    margin-top: 22px;
  }
  .features {
    position: absolute; left: 0; bottom: 0;
    width: 100%; height: 170px;
    background: linear-gradient(180deg, var(--teal-dark), var(--teal-light));
    border-top: 3px solid var(--teal-dark);
    display: grid;
    grid-template-columns: 264px 300px;
    grid-template-rows: 64px 64px;
    padding: 24px 0 0 210px;
    list-style: none;
  }
  .feature {
    display: flex; align-items: center; gap: 14px;
    color: var(--white);
    font-weight: 500;
    font-size: 24px;
  }
  .feature__icon {
    width: 40px; height: 40px; flex: none;
  }
</style>
</head>
<body>
  <main class="label">
    <svg class="label__rule" viewBox="0 0 880 90" aria-hidden="true">
      <path d="M0 16 H360 Q400 16 440 70 Q480 16 520 16 H880" fill="none" stroke="#3a9a78" stroke-width="5"/>
    </svg>

    <header class="brand">
      <div class="brand__name">VERDALIS</div>
      <div class="brand__tagline">Soin Animal</div>
    </header>

    <section class="product">
      <h1 class="product__name">TENDRESSE APAISANTE</h1>
      <p class="product__dose">CBD 150 MG</p>
    </section>

    <ul class="features">
      <li class="feature">
        <svg class="feature__icon" viewBox="0 0 40 40" aria-hidden="true">
          <circle cx="20" cy="20" r="20" fill="#fff"/>
          <circle cx="20" cy="20" r="4" fill="#3a9a78"/>
          <circle cx="20" cy="10" r="4.5" fill="#3a9a78"/>
          <circle cx="11.5" cy="25" r="4.5" fill="#3a9a78"/>
          <circle cx="28.5" cy="25" r="4.5" fill="#3a9a78"/>
        </svg>
        Anti-Stress
      </li>
      <li class="feature">
        <svg class="feature__icon" viewBox="0 0 40 40" aria-hidden="true">
          <circle cx="20" cy="20" r="20" fill="#fff"/>
          <path d="M11 27 C11 16 19 11 29 11 C29 22 22 28 11 27 Z" fill="#3a9a78"/>
          <path d="M13 26 L24 16" stroke="#fff" stroke-width="1.6"/>
        </svg>
        100% naturel
      </li>
      <li class="feature">
        <svg class="feature__icon" viewBox="0 0 40 40" aria-hidden="true">
          <circle cx="20" cy="20" r="20" fill="#fff"/>
          <path d="M9 17 Q20 25 31 17" fill="none" stroke="#3a9a78" stroke-width="2"/>
          <path d="M18 22 Q18 30 22 30 Q26 30 25 22" fill="none" stroke="#3a9a78" stroke-width="2"/>
        </svg>
        A lécher
      </li>
      <li class="feature">
        <svg class="feature__icon" viewBox="0 0 40 40" aria-hidden="true">
          <circle cx="20" cy="20" r="20" fill="#fff"/>
          <path d="M10 30 V16 Q10 9 20 9 Q30 9 30 16 V30 Z" fill="#3a9a78"/>
          <path d="M15 30 V19 M20 30 V16 M25 30 V19" stroke="#fff" stroke-width="1.6"/>
        </svg>
        Beurre de cacahuète
      </li>
    </ul>
  </main>
</body>
</html>
```